Update our business cards to match our awesome new website

Need a new design for company business cards. We have recently revamped our website and would like our business cards to get a refresh too. I've uploaded the company artwork, logo, as well as the Branding Deck to better understand the look & feel of our brand. Please visit the website at hollowbrookestatesmi.com.

Industry/Entity Type

Real Estate

Contact Information for Business Card

must use the colors outlined in the Branding Deck uploaded to the site, or the colors of our logo.

Font styles to use
Other font styles liked:
• Calibri

Requirements
Must have
• Required items: Name, title, company logo, address: 218 Fenwick St. Suite 300, Northville, MI 48173, email address: cole@hollowbrookestatesMI.com, company phone 800-555-0193, cell: 248-555-0162
Nice to have
• a more simple design. not complicated
Should not have
• cartoonish characters, or whimsical writing or artwork, stay within our branding colors

```html
<!DOCTYPE html>
<html lang="en">
<head>
<meta charset="utf-8">
<title>Hollowbrook Estates – Business Card</title>
<link rel="stylesheet" href="https://fonts.googleapis.com/css2?family=Carlito:wght@400;700&family=Open+Sans:wght@400;600;700&display=swap">
<style>
  :root {
    --page-bg: #e6e6e6;
    --card-white: #ffffff;
    --card-dark: #231f20;
    --brand-blue: #1f6fba;
    --brand-green: #5a9e3a;
    --leaf-green: #7cc242;
    --text-gray: #444444;
    --text-dark: #2b2b2b;
  }
  * { box-sizing: border-box; margin: 0; padding: 0; }
  html, body { width: 1200px; height: 1200px; overflow: hidden; }
  body {
    background: var(--page-bg);
    font-family: "Open Sans", "Carlito", sans-serif;
    position: relative;
  }
  .card {
    position: absolute;
    left: 200px;
    width: 800px;
    height: 457px;
    border-radius: 30px;
  }
  .card--front { top: 118px; background: var(--card-white); }
  .card--back { top: 625px; background: var(--card-dark); }

  .brand {
    position: absolute;
    left: 62px;
    top: 205px;
    width: 320px;
    display: flex;
    align-items: center;
    gap: 12px;
  }
  .brand__dot {
    width: 22px; height: 22px; border-radius: 50%;
    background: var(--leaf-green);
    flex: none;
  }
  .brand__name {
    font-family: "Carlito", sans-serif;
    font-weight: 400;
    font-size: 31px;
    color: var(--text-dark);
    white-space: nowrap;
  }
  .divider {
    position: absolute;
    left: 412px; top: 131px;
    width: 1.5px; height: 194px;
    background: var(--brand-blue);
  }
  .contact {
    position: absolute;
    left: 441px; top: 124px;
    color: var(--text-gray);
  }
  .contact__name {
    font-weight: 600;
    font-size: 24px;
    letter-spacing: 0.3px;
    color: var(--brand-blue);
    line-height: 1.1;
  }
  .contact__title {
    font-size: 16px;
    color: var(--brand-green);
    line-height: 1.4;
  }
  .contact__address {
    margin-top: 12px;
    font-size: 16px;
    line-height: 22px;
  }
  .contact__list {
    list-style: none;
    margin-top: 10px;
    font-size: 16px;
  }
  .contact__list li {
    display: flex; align-items: center;
    height: 23px;
  }
  .contact__list svg {
    width: 14px; height: 14px;
    margin-right: 12px;
    fill: var(--brand-blue);
    flex: none;
  }

  .back-brand {
    position: absolute;
    left: 0; right: 0; top: 190px;
    text-align: center;
    font-family: "Carlito", sans-serif;
    font-weight: 400;
    font-size: 64px;
    color: var(--leaf-green);
  }
  .social {
    position: absolute;
    left: 0; right: 0; top: 388px;
    display: flex; justify-content: center; gap: 4px;
  }
  .social__item {
    width: 27px; height: 27px; border-radius: 50%;
    background: var(--brand-blue);
  }
</style>
</head>
<body>
  <section class="card card--front">
    <div class="brand">
      <span class="brand__dot"></span>
      <span class="brand__name">Hollowbrook Estates</span>
    </div>
    <div class="divider"></div>
    <div class="contact">
      <div class="contact__name">DANIEL REYES</div>
      <div class="contact__title">President</div>
      <div class="contact__address">218 Fenwick St. Suite 300<br>Northville, MI 48173</div>
      <ul class="contact__list">
        <li><svg viewBox="0 0 16 16"><path d="M3.5 1l3 3-1.6 2.1a9 9 0 005 5L12 9.5l3 3-2 2.3C7 15 1 9 1.2 3z"/></svg>800-555-0193</li>
        <li><svg viewBox="0 0 16 16"><path d="M4 0h8a1 1 0 011 1v14a1 1 0 01-1 1H4a1 1 0 01-1-1V1a1 1 0 011-1zm1 2v10h6V2z"/></svg>248-555-0162</li>
        <li><svg viewBox="0 0 16 16"><path d="M1 3h14v10H1zm1.5 1.5L8 9l5.5-4.5v-.1h-11z"/></svg>cole@hollowbrookestatesMI.com</li>
        <li><svg viewBox="0 0 16 16"><circle cx="8" cy="8" r="7"/><path d="M5 4c2 0 3 1 2 3s-3 1-3 3 1 2 0 3" stroke="#fff" stroke-width="1.4" fill="none"/></svg>hollowbrookestatesmi.com</li>
      </ul>
    </div>
  </section>

  <section class="card card--back">
    <div class="back-brand">Hollowbrook Estates</div>
    <div class="social" aria-label="Social links">
      <span class="social__item"></span>
      <span class="social__item"></span>
      <span class="social__item"></span>
      <span class="social__item"></span>
    </div>
  </section>
</body>
</html>
```